Law Firm Header Revision

Task: Redesign my law firm Word document header (modern, succinct, logo-first, easy address updates)

I need you to revise and modernize my Microsoft Word document header for Law Office of Bryce Holloman, PLLC. The result should look professional and clean on letters (including Letters of Protection), with the logo as the main focus and the text kept succinct.

Goals:
1. Create a modern, minimal header that feels premium and uncluttered.
Make the logo the most visually dominant element.
Reduce the visual weight of the contact/address block so it doesn’t distract from the document.
Make the address easy to change later (I’m moving offices soon) while keeping the same header design.

2. Content to include (keep all info accurate):
Law Office of Bryce Holloman, PLLC
615 Marrowfield Ave. Ste #300-214, Houston, TX 77019
Office: 832.555.0143
Direct: 713.555.0186
Fax: 832.555.0127
Bhollomanlaw.com

3. Layout requirements:
Provide 3 header style options:
Logo left + contact info right
Centered logo + single concise contact line below
Logo left + firm name prominent + minimal contact line
The primary line near the logo should be minimal (preferably website + main office phone).
The address should be easy to update in one place without redesigning the header. Prefer either:
Move the full address to the footer, or
Put the address in a single dedicated line/block so I can edit it once and keep the layout unchanged.
4. Build constraints:
Must be achievable using standard Microsoft Word tools only (header/footer, tables, alignment, fonts, spacing). No advanced graphics software.
Provide exact header text, plus step-by-step Word instructions for each option:
Font recommendations + sizes
Alignment
Spacing
Table setup (if used)
How to keep it consistent across pages

5. Deliverable:
For each of the 3 options, provide:
The exact header content (with line breaks)
Formatting specs (fonts, sizes, spacing)
Word build steps so I can recreate it reliably and keep the logo as the focal point.

```html
<!DOCTYPE html>
<html lang="en">
<head>
<meta charset="utf-8">
<title>Law Office of Bryce Holloman, PLLC — Letterhead Options</title>
<link href="https://fonts.googleapis.com/css2?family=Arimo:ital,wght@0,400;0,700;1,700&display=swap" rel="stylesheet">
<style>
:root{
  --navy:#0c1625;
  --ink:#1b2230;
  --rule:#bfc3c9;
  --paper:#ffffff;
  --canvas:#ffffff;
}
*{box-sizing:border-box;margin:0;padding:0}
html,body{width:1200px;height:4231px;overflow:hidden;background:var(--canvas)}
body{position:relative;font-family:"Arimo",Arial,sans-serif;color:var(--ink)}
.sheet{position:absolute;left:98px;width:976px;height:1264px;background:var(--paper);box-shadow:0 2px 8px rgba(0,0,0,.18);overflow:hidden}
.sheet--one{top:77px}.sheet--two{top:1397px}.sheet--three{top:2722px}
.header{position:absolute;left:0;top:0;width:100%;height:182px;border-bottom:1.5px solid var(--rule)}
.stripes{position:absolute;left:0;top:0}
.brand{position:absolute;display:flex;align-items:center;gap:14px}
.brand__mark{width:88px;height:88px;background:var(--navy)}
.brand__name{font-size:50px;font-weight:400;color:var(--navy);letter-spacing:-.5px;white-space:nowrap}
.contact-stack{position:absolute;right:0;top:0;width:243px;height:182px}
.contact-cell{height:91px;display:flex;align-items:center;gap:14px;padding-left:30px;font-size:14px}
.contact-stack--dark .contact-cell{background:var(--navy);color:#fff}
.contact-stack--dark .contact-cell+.contact-cell{border-top:2px solid #fff}
.contact-stack--light{border-left:1.5px solid var(--rule)}
.contact-stack--light .contact-cell+.contact-cell{border-top:1.5px solid var(--rule)}
.icon{width:16px;height:16px;flex:none}
.contact-tabs{position:absolute;top:131px;left:269px;display:flex;gap:3px}
.contact-tab{height:50px;background:var(--navy);color:#fff;display:flex;align-items:center;gap:14px;padding:0 30px;font-size:14px}
.firm-name{position:absolute;left:74px;top:124px;font-size:21px;font-weight:700;color:var(--ink)}
.details{position:absolute;top:1130px;left:0;width:100%;font-size:14px;line-height:1.8}
.detail{position:absolute;top:0;display:flex;gap:18px}
.detail .icon{margin-top:5px}
.footer{position:absolute;left:0;bottom:0;width:100%;height:78px;border-top:1.5px solid var(--rule)}
.footer__title{position:absolute;left:75px;top:29px;font-size:14px;font-weight:700;font-style:italic}
.footer__page{position:absolute;right:0;top:0;height:100%;width:101px;display:flex;align-items:center;justify-content:center;font-size:14px}
.footer__page--dark{background:var(--navy);color:#fff;top:-1px;height:78px}
.footer__page--dark.short{top:17px;height:45px}
</style>
</head>
<body>

<svg width="0" height="0" style="position:absolute">
  <defs>
    <symbol id="i-phone" viewBox="0 0 16 16"><path d="M4 1.5l2.2 3-1.4 1.6c.8 1.9 2.3 3.4 4.2 4.2l1.6-1.4 3 2.2-1.2 2.6C7 13.4 2.6 9 1.5 2.7z" fill="none" stroke="currentColor" stroke-width="1.2" stroke-linejoin="round"/></symbol>
    <symbol id="i-globe" viewBox="0 0 16 16"><g fill="none" stroke="currentColor" stroke-width="1.2"><circle cx="8" cy="8" r="6.5"/><ellipse cx="8" cy="8" rx="2.8" ry="6.5"/><path d="M1.5 8h13M2.5 4.8h11M2.5 11.2h11"/></g></symbol>
    <symbol id="i-pin" viewBox="0 0 16 16"><g fill="none" stroke="currentColor" stroke-width="1.2"><path d="M8 15s5-5.2 5-8.8A5 5 0 0 0 3 6.2C3 9.8 8 15 8 15z"/><circle cx="8" cy="6.3" r="1.8"/></g></symbol>
    <symbol id="i-fax" viewBox="0 0 16 16"><g fill="none" stroke="currentColor" stroke-width="1.2"><rect x="1" y="5" width="14" height="9" rx="1"/><path d="M4 5V1.5h6l2 2V5M4 8h4M4 11h4"/><rect x="10" y="8" width="3" height="3"/></g></symbol>
  </defs>
</svg>

<!-- Option 1: logo left, contact right -->
<section class="sheet sheet--one">
  <header class="header">
    <svg class="stripes" width="976" height="182" aria-hidden="true">
      <polygon points="0,65 42,182 0,182" fill="var(--navy)"/>
      <line x1="0" y1="112" x2="25" y2="182" stroke="#fff" stroke-width="2"/>
    </svg>
    <div class="brand" style="left:51px;top:45px">
      <span class="brand__mark"></span><span class="brand__name">BRYCE HOLLOMAN</span>
    </div>
    <div class="contact-stack contact-stack--dark">
      <div class="contact-cell"><svg class="icon"><use href="#i-phone"/></svg>Office - 832.555.0143</div>
      <div class="contact-cell"><svg class="icon"><use href="#i-globe"/></svg>Bhollomanlaw.com</div>
    </div>
    <svg class="stripes" style="left:auto;right:0" width="60" height="182" aria-hidden="true">
      <polygon points="60,90 60,182 26,182" fill="#fff"/>
      <polygon points="60,108 60,182 34,182" fill="var(--navy)"/>
      <line x1="60" y1="96" x2="20" y2="182" stroke="#fff" stroke-width="2"/>
    </svg>
  </header>
  <div class="details">
    <div class="detail" style="left:75px"><svg class="icon"><use href="#i-pin"/></svg><span>615 Marrowfield Ave. Ste #300-214<br>Houston, TX 77019</span></div>
    <div class="detail" style="left:423px"><svg class="icon"><use href="#i-phone"/></svg><span>Direct - 713.555.0186</span></div>
    <div class="detail" style="left:726px"><svg class="icon"><use href="#i-fax"/></svg><span>Fax - 832.555.0127</span></div>
  </div>
  <footer class="footer">
    <svg class="stripes" style="top:auto;bottom:0" width="976" height="78" aria-hidden="true">
      <polygon points="0,44 16,78 0,78" fill="var(--navy)"/>
      <line x1="960" y1="78" x2="976" y2="50" stroke="var(--navy)" stroke-width="2"/>
    </svg>
    <span class="footer__title">Letter of Protection</span>
    <span class="footer__page footer__page--dark">Page 01</span>
  </footer>
</section>

<!-- Option 2: centered logo, single contact line -->
<section class="sheet sheet--two">
  <header class="header">
    <svg class="stripes" width="976" height="182" aria-hidden="true">
      <polygon points="0,0 18,0 62,182 28,182 0,64" fill="var(--navy)"/>
      <line x1="0" y1="40" x2="34" y2="182" stroke="#fff" stroke-width="2"/>
      <line x1="0" y1="90" x2="22" y2="182" stroke="var(--navy)" stroke-width="2"/>
      <polygon points="976,0 958,0 914,182 948,182 976,64" fill="var(--navy)"/>
      <line x1="976" y1="40" x2="942" y2="182" stroke="#fff" stroke-width="2"/>
      <line x1="976" y1="90" x2="954" y2="182" stroke="var(--navy)" stroke-width="2"/>
    </svg>
    <div class="brand" style="left:0;right:0;justify-content:center;top:38px;gap:10px">
      <span class="brand__mark" style="width:62px;height:62px"></span><span class="brand__name" style="font-size:38px">BRYCE HOLLOMAN</span>
    </div>
    <div class="contact-tabs">
      <div class="contact-tab" style="width:238px"><svg class="icon"><use href="#i-phone"/></svg>Office - 832.555.0143</div>
      <div class="contact-tab" style="width:199px"><svg class="icon"><use href="#i-globe"/></svg>Bhollomanlaw.com</div>
    </div>
  </header>
  <div class="details">
    <div class="detail" style="left:75px"><svg class="icon"><use href="#i-pin"/></svg><span>615 Marrowfield Ave. Ste #300-214<br>Houston, TX 77019</span></div>
    <div class="detail" style="left:423px"><svg class="icon"><use href="#i-phone"/></svg><span>Direct - 713.555.0186</span></div>
    <div class="detail" style="left:726px"><svg class="icon"><use href="#i-fax"/></svg><span>Fax - 832.555.0127</span></div>
  </div>
  <footer class="footer">
    <svg class="stripes" style="top:auto;bottom:0" width="976" height="78" aria-hidden="true">
      <polygon points="0,36 20,78 0,78" fill="var(--navy)"/>
      <line x1="0" y1="52" x2="12" y2="78" stroke="#fff" stroke-width="2"/>
      <polygon points="976,36 956,78 976,78" fill="var(--navy)"/>
      <line x1="976" y1="52" x2="964" y2="78" stroke="#fff" stroke-width="2"/>
    </svg>
    <span class="footer__title">Letter of Protection</span>
    <span class="footer__page">Page 01</span>
  </footer>
</section>

<!-- Option 3: logo left, firm name prominent -->
<section class="sheet sheet--three">
  <header class="header">
    <svg class="stripes" width="976" height="182" aria-hidden="true">
      <polygon points="0,65 42,182 0,182" fill="var(--navy)"/>
      <line x1="0" y1="112" x2="25" y2="182" stroke="#fff" stroke-width="2"/>
    </svg>
    <div class="brand" style="left:74px;top:28px;gap:10px">
      <span class="brand__mark" style="width:70px;height:70px"></span><span class="brand__name" style="font-size:42px">BRYCE HOLLOMAN</span>
    </div>
    <div class="firm-name">Law Office of Bryce Holloman, PLLC</div>
    <div class="contact-stack contact-stack--light">
      <div class="contact-cell"><svg class="icon"><use href="#i-phone"/></svg>Office - 832.555.0143</div>
      <div class="contact-cell"><svg class="icon"><use href="#i-globe"/></svg>Bhollomanlaw.com</div>
    </div>
    <svg class="stripes" style="left:auto;right:0" width="60" height="182" aria-hidden="true">
      <polygon points="60,96 60,182 20,182" fill="var(--navy)"/>
      <line x1="60" y1="120" x2="36" y2="182" stroke="#fff" stroke-width="2"/>
    </svg>
  </header>
  <div class="details">
    <div class="detail" style="left:75px"><svg class="icon"><use href="#i-pin"/></svg><span>615 Marrowfield Ave. Ste #300-214<br>Houston, TX 77019</span></div>
    <div class="detail" style="left:423px"><svg class="icon"><use href="#i-phone"/></svg><span>Direct - 713.555.0186</span></div>
    <div class="detail" style="left:726px"><svg class="icon"><use href="#i-fax"/></svg><span>Fax - 832.555.0127</span></div>
  </div>
  <footer class="footer">
    <svg class="stripes" style="top:auto;bottom:0" width="976" height="78" aria-hidden="true">
      <polygon points="0,44 16,78 0,78" fill="var(--navy)"/>
    </svg>
    <span class="footer__title">Letter of Protection</span>
    <span class="footer__page footer__page--dark short" style="right:0">Page 01</span>
  </footer>
</section>

</body>
</html>
```